Postcard: Live Ever Kinder

Text for front: HOW TO CHANGE THE WORLD IN ONE [note: the word "one" should be underlined] STEPHint: It's up to you...[Note: add arrow or something to indicate "turn over"]Text for back: You're going to spend your entire life with someone you can never get away from. (Guess who?) Wouldn't you rather that person #LiveEverKinder than judgmental or critical? BE the change you want to see! Visit www.LiveEverKinder-hub.com for daily Bright Pebbles and community. PLEASE JOIN US![Note: add logo to left half of back side]Font preference for text: Josefin sans

Target Market(s)

People who would be attracted to Calvera church - unitarian universalist message. It's spiritual without being overtly religious, so the target market is probably early 30s and up but ideally won't turn off Millennials (folks under 30). It should attract attention of people who are open-minded and committed to progressive social change, tired of an atmosphere of hate-mongering and divisiveness.

Requirements
Nice to have
• It would be nice to convey a sense of challenge - there is an idea of "bright pebbles" so something related to fire/sparks is appropriate. This is meant to evoke a deeper, divine love more than a sense of romantic love. This love is more fierce than fluffy! Yet it calls us to be our best selves.
Should not have
• Please avoid excessive pink - just the logo is enough, as this design needs to appeal to men as well as women.

```html
<!DOCTYPE html>
<html lang="en">
<head>
<meta charset="utf-8">
<title>Live Ever Kinder – Postcard</title>
<link rel="stylesheet" href="https://fonts.googleapis.com/css2?family=Josefin+Sans:wght@300;400;700&family=Marcellus&family=Marcellus+SC&display=swap">
<style>
  :root {
    --page: #ffffff;
    --card-light: #97828a;
    --card-mid: #8a747c;
    --card-dark: #7c6870;
    --gold: #ecd6a4;
    --gold-bright: #f4e2b2;
    --arrow-light: #d9aec3;
    --arrow-dark: #7e5a6c;
  }
  * { margin: 0; padding: 0; box-sizing: border-box; }
  html, body {
    width: 899px; height: 1200px; overflow: hidden;
    background: var(--page);
  }
  .canvas { position: relative; width: 899px; height: 1200px; }

  .card {
    position: absolute; left: 33px; width: 843px; height: 572px;
    overflow: hidden; color: var(--gold);
  }
  .card--front { top: 33px; }
  .card--back { top: 618px; }

  .card__texture {
    position: absolute; inset: 0;
    background:
      radial-gradient(ellipse at 30% 25%, var(--card-light), transparent 60%),
      radial-gradient(ellipse at 80% 80%, var(--card-dark), transparent 65%),
      var(--card-mid);
  }

  .headline {
    position: absolute; left: 0; right: 0; top: 58px;
    text-align: center;
    font-family: "Marcellus", serif;
    font-size: 66px; line-height: 80px; letter-spacing: 3px;
    color: var(--gold);
  }
  .headline__one {
    font-family: "Josefin Sans", sans-serif; font-weight: 700;
    color: var(--gold-bright);
    text-decoration: underline; text-decoration-thickness: 3px;
    text-underline-offset: 6px;
    letter-spacing: 1px; margin-right: 14px;
  }

  .turn-arrow { position: absolute; left: 385px; top: 300px; width: 160px; height: 130px; }

  .hint {
    position: absolute; left: 0; right: 0; top: 445px; text-align: center;
    font-family: "Marcellus SC", serif; font-size: 40px; letter-spacing: 2px;
  }

  .brand-mark {
    position: absolute; left: 48px; top: 80px; width: 390px; height: 360px;
    display: flex; flex-direction: column; align-items: center; justify-content: center; gap: 18px;
  }
  .brand-mark__dot { width: 18px; height: 18px; border-radius: 50%; background: var(--gold); }
  .brand-mark__name {
    font-family: "Josefin Sans", sans-serif; font-weight: 400;
    font-size: 40px; letter-spacing: 2px; color: var(--gold);
  }

  .message {
    position: absolute; left: 455px; top: 52px; width: 375px;
    font-family: "Josefin Sans", sans-serif; font-weight: 300;
    font-size: 21px; line-height: 28px;
  }
  .message p + p { margin-top: 26px; }
  .message__visit { text-align: center; margin-top: 26px; }
  .message__url { font-weight: 400; font-size: 24px; line-height: 32px; }

  .join {
    position: absolute; left: 0; right: 0; top: 490px; text-align: center;
    font-family: "Marcellus", serif; font-size: 50px; letter-spacing: 4px;
  }
</style>
</head>
<body>
<main class="canvas">

  <section class="card card--front" aria-label="Postcard front">
    <div class="card__texture" role="img" aria-label="Mauve handmade paper texture"></div>
    <h1 class="headline">HOW TO CHANGE<br>THE WORLD IN<br><span class="headline__one">ONE</span>STEP</h1>
    <svg class="turn-arrow" viewBox="0 0 160 130" aria-hidden="true">
      <defs>
        <linearGradient id="arrow-fill" x1="0" y1="0" x2="1" y2="1">
          <stop offset="0" stop-color="var(--arrow-dark)"/>
          <stop offset="0.55" stop-color="var(--arrow-light)"/>
          <stop offset="1" stop-color="var(--arrow-dark)"/>
        </linearGradient>
      </defs>
      <path d="M28 4 C0 30 4 88 70 92 L102 92 L102 74 L150 104 L102 128 L102 112 L70 112 C10 112 -6 50 28 4 Z" fill="url(#arrow-fill)"/>
    </svg>
    <p class="hint">Hint: It's up to you...</p>
  </section>

  <section class="card card--back" aria-label="Postcard back">
    <div class="card__texture" role="img" aria-label="Mauve handmade paper texture"></div>
    <div class="brand-mark">
      <span class="brand-mark__dot"></span>
      <span class="brand-mark__name">Live Ever Kinder</span>
    </div>
    <div class="message">
      <p>You're going to spend your<br>entire life with someone you<br>can never get away from.<br>(Guess who?)</p>
      <p>Wouldn't you rather that<br>person #LiveEverKinder than<br>judgmental or critical? BE the<br>change you want to see!</p>
      <p class="message__visit">Visit<br><span class="message__url">www.LiveEverKinder-hub.com</span><br>for daily Bright Pebbles<br>and community.</p>
    </div>
    <p class="join">PLEASE JOIN US</p>
  </section>

</main>
</body>
</html>
```